Life Coaching and Career Coaching company needs new website with bold, modern, videos

We need a whole new website that is heavy on video. We are a small company who sells personal wellbeing services like career coaching, life coaching, and group coaching programs. The programs all help people design a better life.
FULL BRIEF ATTACHED and STYLE GUIDE
Also, look at https://www.brightfennel.com/coaching and galdrove.com and https://www.marnwick.life/ for a small amount of inspiration.

Industry/Entity Type

personal well-being/life coaching/career coaching

Number of Pages Required

3 page

Other font styles liked:
• fonts are in the brief

Requirements
Must have
• read the brief please - it's all in there. (things like the look, feel, how it will have lots of video, etc,)
Nice to have
• something really different looking and breakthrough. visually stunning. very trustworthy. Please read the brief, its all in there.
Should not have
• should not look like other life coaching websites. must have video!

```html
<!DOCTYPE html>
<html lang="en">
<head>
<meta charset="utf-8">
<title>Kindpath Collective — Home</title>
<link href="https://fonts.googleapis.com/css2?family=Comfortaa:wght@400;700&family=Didact+Gothic&family=Great+Vibes&family=Poppins:ital,wght@1,300&display=swap" rel="stylesheet">
<style>
:root{
  --coral:#f06565;
  --blush:#fbe4e0;
  --blush-card:#fbeaea;
  --teal:#0d5656;
  --teal-btn:#2e7272;
  --ink:#1f1f1f;
  --plum:#6b2a45;
  --stone:#f2f1ef;
  --mist:#f2f6f8;
  --line:#9aaeb0;
  --white:#ffffff;
}
*{margin:0;padding:0;box-sizing:border-box}
html,body{width:1200px;height:1200px;overflow:hidden;background:var(--white)}
body{font-family:"Didact Gothic",sans-serif;color:var(--ink)}
.page{position:absolute;left:484px;top:33px;width:382px;height:1825px;transform:scale(.625);transform-origin:0 0;background:var(--white);overflow:hidden;box-shadow:0 0 6px rgba(0,0,0,.04)}
.abs{position:absolute}
.heading{font-family:"Comfortaa",sans-serif;font-weight:400;color:var(--ink)}
.sub{font-size:3.6px;line-height:6.4px;color:var(--plum);text-align:center}
.body-text{font-size:3.6px;line-height:7px;color:#333}
.rule{position:absolute;height:.6px;background:var(--coral)}
.photo{position:absolute}
.btn-solid{position:absolute;display:flex;align-items:center;justify-content:center;font-size:3.8px;color:var(--white);background:var(--teal)}
.btn-ghost{position:absolute;display:flex;align-items:center;justify-content:center;font-size:3.8px;border:.6px solid var(--teal-btn);color:var(--teal-btn)}
.center{left:0;width:382px;text-align:center}
/* nav */
.topline{left:0;top:0;width:382px;height:1.2px;background:var(--coral)}
.nav-link{font-size:4px;top:18px;color:var(--ink)}
.brand{font-family:"Comfortaa",sans-serif;font-size:8.5px;font-weight:700;letter-spacing:.3px;color:var(--ink)}
/* hero */
.hero-band{left:0;top:61px;width:382px;height:173px;background:var(--blush)}
.hero-card{left:167px;top:82px;width:160px;height:101px;background:var(--white);box-shadow:0 1px 4px rgba(0,0,0,.06)}
.hero-title{font-family:"Comfortaa",sans-serif;font-weight:700;font-size:12.5px;line-height:15px;text-align:center;margin-top:16px}
.play{position:absolute;width:20px;height:20px;border:1px solid var(--white);border-radius:50%;display:flex;align-items:center;justify-content:center}
.play-sm{width:11px;height:11px;border-width:.6px}
/* service cards */
.svc-img{position:absolute}
.svc-body{position:absolute;background:var(--blush-card);text-align:center}
.svc-title{font-family:"Comfortaa",sans-serif;font-size:6.2px;line-height:8.5px;margin-top:6px}
.svc-text{font-size:3.5px;line-height:6.8px;color:#444;padding:3px 5px 0}
.pill{position:absolute;height:10px;border-radius:6px;background:var(--teal-btn);color:var(--white);font-size:3.5px;display:flex;align-items:center;justify-content:center}
/* scale section */
.stone{left:0;top:539px;width:382px;height:423px;background:var(--stone)}
.eyebrow{font-size:3.2px;letter-spacing:.5px;color:var(--coral)}
.feature-title{font-family:"Comfortaa",sans-serif;font-size:7.6px}
.feature-card{position:absolute;background:var(--white)}
.know{position:absolute;font-size:3.4px;letter-spacing:.8px;color:var(--teal-btn)}
.know-line{position:absolute;height:.5px;background:var(--teal-btn)}
/* cta */
.cta{left:0;top:962px;width:382px;height:119px;background:var(--coral)}
.cta-title{font-family:"Poppins",sans-serif;font-style:italic;font-weight:300;font-size:9.6px;color:var(--white)}
/* programs */
.programs{left:0;top:1081px;width:382px;height:209px;background:var(--mist)}
.tag-v{position:absolute;background:var(--white);font-family:"Comfortaa",sans-serif;font-size:5.4px;display:flex;align-items:center;justify-content:center;writing-mode:vertical-rl}
.tag-up{transform:rotate(180deg)}
.caption{position:absolute;font-size:3.4px;line-height:6.6px;text-align:center;color:#555}
/* coach */
.coach-frame{left:127px;top:1318px;width:184px;height:176px;border:.6px solid var(--line)}
.coach-card{left:161px;top:1338px;width:188px;height:136px;background:var(--white);box-shadow:0 1px 6px rgba(0,0,0,.08)}
.script{font-family:"Great Vibes",cursive;font-size:10px;color:var(--coral)}
/* testimonials */
.quote-mark{font-family:"Comfortaa",sans-serif;font-size:70px;line-height:1;color:#f8dcdc;font-weight:700}
/* footer */
.footer{left:0;top:1759px;width:382px;height:66px;background:var(--teal);border-top:1px solid var(--coral)}
.foot-link{position:absolute;top:41px;font-size:3.6px;color:#cfe0e0}
.social{position:absolute;top:20px;width:9px;height:9px;border-radius:50%;background:var(--white)}
</style>
</head>
<body>
<main class="page">

  <!-- Navigation -->
  <div class="abs topline"></div>
  <span class="abs nav-link" style="left:44px">Home</span>
  <span class="abs nav-link" style="left:73px">About</span>
  <span class="abs nav-link" style="left:102px">Coaching</span>
  <span class="abs brand" style="left:151px;top:14px">KINDPATH</span>
  <span class="abs nav-link" style="left:245px">Programs</span>
  <span class="abs nav-link" style="left:279px">Blog</span>
  <div class="btn-ghost" style="left:303px;top:14px;width:35px;height:13px;border-color:var(--plum);color:var(--plum)">Contact Us</div>

  <!-- Hero -->
  <div class="abs hero-band"></div>
  <div class="photo" role="img" aria-label="Coach presenting to a seated group in a bright studio" style="left:0;top:41px;width:228px;height:168px;background:linear-gradient(135deg,#d9dcd8,#8e8f88 55%,#3b3734)"></div>
  <div class="play" style="left:95px;top:114px"><svg width="7" height="8" viewBox="0 0 7 8"><path d="M0 0L7 4L0 8Z" fill="#fff"/></svg></div>
  <section class="abs hero-card">
    <h1 class="hero-title">Real insights mean<br>real results</h1>
    <p class="sub" style="color:#333;margin-top:3px;line-height:5.4px">Quickly learn how it works or scroll below to browse<br>services and coaches.</p>
  </section>
  <div class="btn-solid" style="left:220px;top:153px;width:54px;height:13px">Book A Free Call</div>

  <!-- Who we are -->
  <h2 class="abs heading center" style="top:257px;font-size:11px">Who we Are</h2>
  <p class="abs sub center" style="top:271px">Lorem ipsum dolor sit amet, consectetur adipiscing elit. Quisque pharetra sit<br>amet libero ut consectetur. Donec egestas nunc</p>
  <div class="rule" style="left:165px;top:289px;width:50px"></div>
  <p class="abs body-text" style="left:60px;top:297px;width:262px;text-align:center">Lorem ipsum dolor sit amet, consectetur adipiscing elit. Quisque pharetra sit amet libero ut consectetur. Donec egestas nunc a dui scelerisque, vel fringilla nulla porttitor. Maecenas laoreet ut dui vel placerat. Cras feugiat placerat tortor, non ornare nunc blandit sit amet. Sed convallis magna mauris, non pretium magna imperdiet eu. Nulla in efficitur elit. Nam non blandit eros. Mauris sed ante eu enim condimentum volutpat. Nullam ultrices quam tempus odio euismod, eget pretium libero ultrices. Sed non magna enim. In pulvinar maximus purus, a viverra mauris.</p>

  <div class="svc-img" role="img" aria-label="Group session video still" style="left:60px;top:371px;width:74px;height:43px;border-radius:22px 0 0 0;background:linear-gradient(160deg,#c9b8a8,#5a4538)"></div>
  <div class="play play-sm" style="left:91px;top:386px"><svg width="4" height="5" viewBox="0 0 7 8"><path d="M0 0L7 4L0 8Z" fill="#fff"/></svg></div>
  <div class="svc-body" style="left:65px;top:414px;width:64px;height:65px">
    <h3 class="svc-title">On-demand<br>specialists</h3>
    <p class="svc-text" style="line-height:6.6px">Lorem ipsum dolor sit amet, consectetur adipiscing elit. Quisque pharetra sit amet libero ut consectetur.</p>
  </div>
  <div class="pill" style="left:71px;top:474px;width:52px">Get Started</div>

  <div class="svc-img" role="img" aria-label="Coach leading a workshop" style="left:145px;top:350px;width:91px;height:47px;border-radius:4px 4px 0 0;background:linear-gradient(170deg,#e4e4e2,#8a8c92 60%,#3e4048)"></div>
  <div class="svc-body" style="left:145px;top:397px;width:91px;height:95px">
    <h3 class="svc-title" style="margin-top:9px">Dedicated 1:1<br>Coaching</h3>
    <p class="svc-text" style="padding:3px 7px 0">Lorem ipsum dolor sit amet, consectetur adipiscing elit. Quisque pharetra sit amet libero ut consectetur. Donec egestas nunc a dui scelerisque, vel fringilla nulla porttitor. Maecenas laoreet ut dui vel placerat.</p>
  </div>
  <div class="pill" style="left:161px;top:487px;width:59px">Get Started</div>

  <div class="svc-img" role="img" aria-label="Team reviewing results in an office" style="left:247px;top:371px;width:75px;height:43px;border-radius:0 22px 0 0;background:linear-gradient(200deg,#d6d8dc,#777b84 55%,#2e3038)"></div>
  <div class="svc-body" style="left:252px;top:414px;width:65px;height:65px">
    <h3 class="svc-title">Business impact<br>studies</h3>
    <p class="svc-text" style="line-height:6.6px">Lorem ipsum dolor sit amet, consectetur adipiscing elit. Quisque pharetra sit amet libero ut consectetur.</p>
  </div>
  <div class="pill" style="left:258px;top:474px;width:52px">Get Started</div>

  <svg class="abs" style="left:182px;top:511px" width="18" height="4" viewBox="0 0 18 4"><circle cx="1.5" cy="2" r="1" fill="#e8c9c9"/><circle cx="5" cy="2" r="1" fill="#e8c9c9"/><rect x="8" y="1" width="9" height="2" rx="1" fill="#f06565"/></svg>

  <!-- Coaching at scale -->
  <div class="abs stone"></div>
  <h2 class="abs heading center" style="top:566px;font-size:11.5px">How we deploy coaching at scale</h2>
  <p class="abs sub center" style="top:582px">Lorem ipsum dolor sit amet, consectetur adipiscing elit. Quisque pharetra sit amet libero ut<br>consectetur. Donec egestas nunc a dui scelerisque, vel fringilla nulla porttitor.</p>
  <div class="rule" style="left:165px;top:601px;width:52px"></div>

  <p class="abs eyebrow" style="left:58px;top:638px">COACHING SCALE</p>
  <h3 class="abs feature-title" style="left:58px;top:651px">Take a personal assessment</h3>
  <p class="abs body-text" style="left:58px;top:667px;width:116px">Lorem ipsum dolor sit amet, consectetur adipiscing elit. Quisque pharetra sit amet libero ut consectetur. Donec egestas nunc a dui scelerisque, vel fringilla nulla porttitor. Maecenas laoreet ut dui vel placerat.</p>

  <div class="feature-card" style="left:196px;top:632px;width:128px;height:195px"></div>
  <div class="photo" role="img" aria-label="Coaching circle with a laptop in a plant-filled room" style="left:196px;top:632px;width:128px;height:167px;background:linear-gradient(160deg,#cfd5cc,#8f9a8a 50%,#4c5148)"></div>
  <div class="know-line" style="left:256px;top:813.5px;width:24px"></div>
  <span class="know" style="left:285px;top:812px">KNOW MORE</span>

  <div class="feature-card" style="left:58px;top:727px;width:128px;height:194px"></div>
  <div class="photo" role="img" aria-label="Two women holding a yoga pose outdoors by the forest" style="left:58px;top:727px;width:128px;height:167px;background:linear-gradient(180deg,#5e6b55,#8d9a86 55%,#b9b8b3)"></div>
  <div class="know-line" style="left:118px;top:908.5px;width:24px"></div>
  <span class="know" style="left:147px;top:907px">KNOW MORE</span>

  <p class="abs eyebrow" style="left:210px;top:849px">COACHING SCALE</p>
  <h3 class="abs feature-title" style="left:210px;top:862px">Easily find the right Coach</h3>
  <p class="abs body-text" style="left:210px;top:878px;width:116px">Lorem ipsum dolor sit amet, consectetur adipiscing elit. Quisque pharetra sit amet libero ut consectetur. Donec egestas nunc a dui scelerisque, vel fringilla nulla porttitor. Maecenas laoreet ut dui vel placerat.</p>

  <!-- Product offerings -->
  <div class="abs cta"></div>
  <h2 class="abs cta-title center" style="top:985px">Discover our product offerings</h2>
  <p class="abs sub center" style="top:1004px;color:#fde8e8">Lorem ipsum dolor sit amet, consectetur adipiscing elit. Quisque pharetra sit amet libero ut consectetur.<br>Donec egestas nunc a dui scelerisque, vel fringilla nulla porttitor.</p>
  <div class="rule" style="left:165px;top:1023px;width:52px;background:#fbc8c8"></div>
  <div class="btn-solid" style="left:135px;top:1041px;width:53px;height:13px;background:var(--white);color:var(--coral)">Book A Free Call</div>
  <div class="btn-ghost" style="left:193px;top:1041px;width:53px;height:13px;border-color:var(--white);color:var(--white)">Consult Now</div>

  <!-- Programs -->
  <div class="abs programs"></div>
  <h2 class="abs heading" style="left:33px;top:1104px;font-size:11.5px">Our Programs</h2>
  <p class="abs sub" style="left:33px;top:1120px;text-align:left">Lorem ipsum dolor sit amet, consectetur adipiscing elit. Quisque pharetra sit amet libero ut consectetur.<br>Donec egestas nunc a dui scelerisque, vel fringilla nulla porttitor.</p>
  <div class="rule" style="left:33px;top:1139px;width:53px"></div>

  <div class="photo" role="img" aria-label="Friends sharing a warm conversation" style="left:45px;top:1161px;width:78px;height:92px;background:linear-gradient(140deg,#c97b4a,#6e4a3a 55%,#3a3236)"></div>
  <div class="tag-v" style="left:116px;top:1172px;width:12px;height:76px">Connect to Purpose</div>
  <p class="caption" style="left:40px;top:1257px;width:88px">Lorem ipsum dolor sit amet, consectetur adipiscing elit. Quisque pharetra</p>

  <div class="photo" role="img" aria-label="Group practising yoga with raised arms" style="left:150px;top:1157px;width:78px;height:96px;background:linear-gradient(180deg,#eef0f2,#a6abb6 50%,#2f3140)"></div>
  <div class="abs heading" style="left:160px;top:1156px;width:58px;height:9px;background:var(--white);font-size:5.4px;text-align:center;line-height:9px">Reduce Stress</div>
  <p class="caption" style="left:145px;top:1257px;width:88px">Lorem ipsum dolor sit amet, consectetur adipiscing elit. Quisque pharetra</p>

  <div class="photo" role="img" aria-label="Thoughtful woman surrounded by sketched ideas" style="left:258px;top:1161px;width:78px;height:92px;background:linear-gradient(160deg,#f3f1ee,#c8c4c6 55%,#6b4a5c)"></div>
  <div class="tag-v tag-up" style="left:253px;top:1172px;width:12px;height:66px">Think Creatively</div>
  <p class="caption" style="left:253px;top:1257px;width:88px">Lorem ipsum dolor sit amet, consectetur adipiscing elit. Quisque pharetra</p>

  <!-- Coach -->
  <div class="abs coach-frame"></div>
  <div class="photo" role="img" aria-label="Smiling coach seated on a green sofa" style="left:33px;top:1324px;width:137px;height:165px;background:linear-gradient(150deg,#eceae6,#c9c3c6 45%,#7fa39a)"></div>
  <div class="abs coach-card"></div>
  <p class="abs script" style="left:191px;top:1329px">Meet Our Coach</p>
  <h2 class="abs heading" style="left:188px;top:1352px;font-size:11px;line-height:15px">The Human<br>Transformation Platform</h2>
  <p class="abs sub" style="left:188px;top:1385px;text-align:left;width:150px">Lorem ipsum dolor sit amet, consectetur adipiscing elit. Quisque<br>pharetra sit amet libero ut consectetur.</p>
  <div class="rule" style="left:188px;top:1404px;width:53px;background:var(--teal-btn)"></div>
  <p class="abs body-text" style="left:188px;top:1411px;width:156px">Lorem ipsum dolor sit amet, consectetur adipiscing elit. Quisque pharetra sit amet libero ut consectetur. Donec egestas nunc a dui scelerisque, vel fringilla nulla porttitor. Maecenas laoreet ut dui vel placerat.</p>
  <div class="btn-ghost" style="left:188px;top:1445px;width:53px;height:13px">Book A Free Call</div>

  <!-- Testimonials -->
  <h2 class="abs heading center" style="top:1523px;font-size:11px">Client Testimonials</h2>
  <p class="abs sub center" style="top:1540px">Lorem ipsum dolor sit amet, consectetur adipiscing elit. Quisque pharetra sit amet libero ut<br>consectetur. Donec egestas nunc a dui scelerisque, vel fringilla nulla porttitor.</p>
  <div class="rule" style="left:165px;top:1558px;width:52px"></div>

  <p class="abs" style="left:41px;top:1615px;font-size:4.6px;font-weight:700;font-family:'Comfortaa',sans-serif">Noriel Vance</p>
  <p class="abs" style="left:41px;top:1623px;font-size:3.8px">Dover, OR</p>
  <div class="abs" style="left:41px;top:1635px;width:99px;height:.5px;background:#bbb"></div>
  <svg class="abs" style="left:41px;top:1641px" width="30" height="6" viewBox="0 0 30 6">
    <g fill="none" stroke="#333" stroke-width=".4">
      <path id="st" d="M3 .6l.7 1.6 1.7.1-1.3 1.1.4 1.7L3 4.2 1.5 5.1l.4-1.7L.6 2.3l1.7-.1z"/>
      <use href="#st" x="5.8"/><use href="#st" x="11.6"/><use href="#st" x="17.4"/><use href="#st" x="23.2"/>
    </g>
  </svg>
  <span class="abs quote-mark" style="left:104px;top:1670px">”</span>
  <p class="abs body-text" style="left:41px;top:1653px;width:116px;font-style:italic;line-height:8.6px;font-size:3.9px">“Lorem ipsum dolor sit amet, consectetur adipiscing elit. Quisque pharetra sit amet libero ut consectetur. Donec egestas nunc a dui scelerisque, vel fringilla nulla porttitor. Maecenas laoreet ut dui vel placerat”.</p>
  <svg class="abs" style="left:47px;top:1706px" width="22" height="2" viewBox="0 0 22 2"><rect x="0" y=".5" width="5" height="1" fill="#9ab"/><rect x="8" y=".3" width="6" height="1.4" fill="#0d5656"/><rect x="16" y=".5" width="5" height="1" fill="#9ab"/></svg>

  <div class="photo" role="img" aria-label="Client in a knit beanie, laughing" style="left:167px;top:1579px;width:74px;height:147px;background:linear-gradient(180deg,#3a3433,#c79a82 40%,#8d8f93)"></div>
  <div class="play play-sm" style="left:198px;top:1647px"><svg width="4" height="5" viewBox="0 0 7 8"><path d="M0 0L7 4L0 8Z" fill="#fff"/></svg></div>
  <div class="photo" role="img" aria-label="Client video thumbnail" style="left:247px;top:1677px;width:38px;height:49px;background:linear-gradient(160deg,#d7c7b8,#7b5a48)"></div>
  <div class="play play-sm" style="left:260.5px;top:1696px"><svg width="4" height="5" viewBox="0 0 7 8"><path d="M0 0L7 4L0 8Z" fill="#fff"/></svg></div>
  <div class="photo" role="img" aria-label="Client video thumbnail" style="left:290px;top:1677px;width:38px;height:49px;background:linear-gradient(160deg,#c9cfd2,#6d5c52)"></div>
  <div class="play play-sm" style="left:303.5px;top:1696px"><svg width="4" height="5" viewBox="0 0 7 8"><path d="M0 0L7 4L0 8Z" fill="#fff"/></svg></div>
  <div class="photo" role="img" aria-label="Client portrait thumbnail" style="left:333px;top:1677px;width:38px;height:49px;background:linear-gradient(160deg,#eae6e4,#8a4a3e 60%,#5b2a40)"></div>

  <div class="abs" style="left:281px;top:1636px;width:16px;height:.5px;background:#666"></div>
  <span class="abs" style="left:303px;top:1634px;font-size:3.8px">Previous</span>
  <span class="abs" style="left:311px;top:1645px;font-size:3.8px">Next</span>
  <div class="abs" style="left:325px;top:1647px;width:17px;height:.5px;background:#666"></div>

  <!-- Footer -->
  <footer class="abs footer">
    <span class="abs brand" style="left:33px;top:16px;color:var(--white)">KINDPATH</span>
    <p class="abs" style="left:34px;top:37px;font-size:3.4px;line-height:6px;color:#cfe0e0">Copyright © 2024 <span style="color:var(--coral)">Kindpath.</span><br>All rights reserved.</p>
    <span class="social" style="left:298px"></span>
    <span class="social" style="left:312px;background:var(--coral)"></span>
    <span class="social" style="left:326px"></span>
    <span class="social" style="left:339px"></span>
    <span class="foot-link" style="left:172px">Home</span>
    <span class="foot-link" style="left:201px">About</span>
    <span class="foot-link" style="left:229px">Coaching</span>
    <span class="foot-link" style="left:265px">Programs</span>
    <span class="foot-link" style="left:300px">Blog</span>
    <span class="foot-link" style="left:325px">Contact Us</span>
  </footer>

</main>
</body>
</html>
```